Harvest Festival 2017 Poster

We need a poster design for our private school's annual Harvest Festival. We're a progressive school in nyc, with deep community roots and a rich hundred year history. The community cherishes the events and looks forward to seeing what excitement each new year will bring! The posters will be displayed thoughout the school, appealing to a diverse audience of children and their' families.
We'd like a vintage vibe, circa turn of the 20th century (1900s). Please reference the images I've included, which give some inspiration. Also, as pertains to the theme, I'd like a representation of a vintage apple basket, brimming with apples, but with a planet earth nestled inside as the main focal point. Kind of like a words fair meets the harvest...
Also typography should be semi old fashioned looking as well.
COPY - Should Include the following:

Brook & Meadow
Lantern Jubilee of Peoples

October 14th 12:00-4:00pm
Celebrate an Afternoon of Great Food, Music, Entertainment, & Fun

Tickets will be available for sale at Pickup

Target Market(s)

School Community, children and their parents, faculty, etc.

Industry/Entity Type

School

Font styles to use
Other font styles liked:
• Something old world fair, country looking

Colors
ec1f27
fcca95
ffcf3e

Requirements
Must have
• We'd like a vintage vibe, circa turn of the 20th century (1900s). Please reference the images I've included, which give some inspiration. Also, as pertains to the theme, I'd like a representation of a vintage apple basket, brimming with apples, but with a planet earth nestled inside as the main focal point. Kind of like a words fair meets the harvest...
• Also typography should be semi old fashioned looking as well.
• COPY - Should Include the following:
• Brook & Meadow
• Lantern Jubilee of Peoples
• October 14th 12:00-4:00pm
• Celebrate an Afternoon of Great Food, Music, Entertainment, & Fun
• Tickets will be available for sale at Pickup
Nice to have
• Attractive design, draws you in, gets you interested in the event, informs you of important details.
Should not have
• I think that the design ask is pretty straight forward.

```html
<!DOCTYPE html>
<html lang="en">
<head>
<meta charset="utf-8">
<title>Lantern Jubilee of Peoples — Poster</title>
<link rel="stylesheet" href="https://fonts.googleapis.com/css2?family=Rye&family=Yesteryear&family=Arvo:wght@700&family=Oswald:wght@400;500;600&display=swap">
<style>
  :root {
    --stage: #e9e6e2;
    --ink: #2c2236;
    --frame-orange: #ef7a2b;
    --frame-cream: #fce0c0;
    --frame-line: #f39a3a;
    --gold: #ffcf3e;
    --peach: #fcca95;
    --photo-top: #f6b9a6;
    --photo-mid: #f2c49a;
    --photo-low: #d9a070;
  }
  * { margin: 0; padding: 0; box-sizing: border-box; }
  html, body {
    width: 1200px; height: 800px; overflow: hidden;
    background: var(--stage);
  }
  .poster {
    position: absolute;
    left: 350px; top: 25px;
    width: 500px; height: 750px;
    background: var(--ink);
    box-shadow: 0 6px 24px rgba(0,0,0,.18);
  }
  .poster-art { position: absolute; inset: 0; }
  .brand-ribbon-text {
    position: absolute; left: 95px; width: 265px; top: 142px;
    text-align: center;
    font-family: "Rye", serif; font-size: 23px; color: var(--ink);
    letter-spacing: .5px;
  }
  .event-title {
    position: absolute; left: 50px; width: 400px; top: 172px;
    text-align: center;
    font-family: "Yesteryear", cursive; font-size: 62px; line-height: 1;
    color: var(--ink);
  }
  .event-subtitle {
    position: absolute; left: 50px; width: 400px; top: 244px;
    text-align: center;
    font-family: "Arvo", serif; font-weight: 700; font-size: 32px;
    color: var(--ink); letter-spacing: 1px;
  }
  .event-date {
    position: absolute; left: 95px; width: 270px; top: 440px;
    text-align: center;
    font-family: "Oswald", sans-serif; font-weight: 600; font-size: 30px;
    line-height: 1.15; color: var(--ink);
  }
  .event-blurb {
    position: absolute; left: 24px; width: 460px; top: 608px;
    font-family: "Oswald", sans-serif; font-weight: 400; font-size: 15px;
    color: var(--gold);
  }
  .ticket-note {
    position: absolute; left: 44px; width: 440px; top: 632px;
    font-family: "Oswald", sans-serif; font-weight: 500; font-size: 20px;
    color: var(--gold);
  }
</style>
</head>
<body>
  <main class="poster">
    <svg class="poster-art" width="500" height="750" viewBox="0 0 500 750">
      <defs>
        <linearGradient id="photoTone" x1="0" y1="0" x2="0" y2="1">
          <stop offset="0" stop-color="var(--photo-top)"/>
          <stop offset=".55" stop-color="var(--photo-mid)"/>
          <stop offset="1" stop-color="var(--photo-low)"/>
        </linearGradient>
      </defs>
      <path class="frame-outer" fill="var(--frame-orange)"
        d="M70,25 H430 A40 40 0 0 0 470,65 V550 A40 40 0 0 0 430,590 H70 A40 40 0 0 0 30,550 V65 A40 40 0 0 0 70,25Z"/>
      <path class="frame-cream" fill="var(--frame-cream)"
        d="M80,35 H420 A50 50 0 0 0 460,75 V540 A50 50 0 0 0 420,580 H80 A50 50 0 0 0 40,540 V75 A50 50 0 0 0 80,35Z"/>
      <path class="frame-line" fill="var(--frame-line)"
        d="M86,41 H414 A56 56 0 0 0 454,81 V534 A56 56 0 0 0 414,574 H86 A56 56 0 0 0 46,534 V81 A56 56 0 0 0 86,41Z"/>
      <path class="hero-photo" fill="url(#photoTone)" role="img"
        aria-label="Faded warm-toned photograph of a wooden house among bare trees on a grassy slope"
        d="M90,45 H410 A60 60 0 0 0 450,85 V530 A60 60 0 0 0 410,570 H90 A60 60 0 0 0 50,530 V85 A60 60 0 0 0 90,45Z"/>
      <polygon class="brand-ribbon" fill="var(--gold)"
        points="95,138 360,132 350,155 362,180 92,184 104,161"/>
      <polygon class="date-ribbon" fill="var(--gold)"
        points="92,432 368,428 356,478 370,528 90,530 102,480"/>
    </svg>

    <div class="brand-ribbon-text">BROOK &amp; MEADOW</div>
    <h1 class="event-title">Lantern Jubilee</h1>
    <div class="event-subtitle">OF PEOPLES</div>
    <div class="event-date">OCTOBER 14TH<br>12:00-4:00PM</div>
    <p class="event-blurb">Celebrate an Afternoon of Great Food, Music, Entertainment, &amp; Fun</p>
    <p class="ticket-note">Tickets will be available for sale at Pickup</p>
  </main>
</body>
</html>
```